Visitenkarten-Design für Süßigkeiten-Onlineshop
Zielgruppe
Ich werde einen Onlineshop betreiben und Süßigkeiten aus aller Welt verkaufen.
Aufgabenstellung
Mein Logo sollte drauf sein. Die Visitenkarte kann auch bisschen stylischer gestaltet werden. Aber da lasse ich mich auch gerne überraschen.
Man könnte vielleicht noch den Slogan- Süßigkeiten aus aller Welt-
Mein Name sollte drauf stehen,
Jonas Brettel
Lindauer Weg 14
41562 Rabenfeld
E-Mail info@zuckerfuchs-shop.de
Instagram @zuckerfuchs.de
Facebook Zuckerfuchs
Tic Toc @zuckerfuhcs.de

```html
<!DOCTYPE html>
<html lang="de">
<head>
<meta charset="utf-8">
<title>Zuckerfuchs – Visitenkarten</title>
<link rel="stylesheet" href="https://fonts.googleapis.com/css2?family=Fira+Sans+Condensed:wght@500&family=Source+Sans+3:wght@400;600&family=Allura&display=swap">
<style>
  :root {
    --page: #f7f7f7;
    --paper: #ffffff;
    --teal: #6cc3c6;
    --teal-light: #a9dde0;
    --ocean: #2a7a9b;
    --ocean-glow: #7cc3c8;
    --pink: #e8538f;
    --ink: #222222;
    --rule: #444444;
    --stage: #c9c9c9;
  }
  * { margin: 0; padding: 0; box-sizing: border-box; }
  html, body { width: 1200px; height: 2389px; overflow: hidden; }
  body { background: var(--page); position: relative; font-family: "Source Sans 3", sans-serif; color: var(--ink); }

  .wordmark { font-family: "Fira Sans Condensed", sans-serif; font-weight: 500; letter-spacing: 0.12em; text-transform: uppercase; white-space: nowrap; text-align: center; line-height: 1; }
  .slogan { font-family: "Allura", cursive; white-space: nowrap; text-align: center; line-height: 1; }
  .brand-disc { position: absolute; border-radius: 50%; background: var(--teal); }

  /* rules framing the wordmark */
  .rule { position: absolute; height: 1px; }
  .rule-top { background: currentColor; }
  .rule-bottom::before, .rule-bottom::after { content: ""; position: absolute; top: 0; height: 1px; width: calc(50% - 24px); background: currentColor; }
  .rule-bottom::before { left: 0; }
  .rule-bottom::after { right: 0; }
  .rule-bottom .dots { position: absolute; left: 50%; top: -3px; transform: translateX(-50%); display: flex; gap: 8px; align-items: center; }
  .rule-bottom .dots i { display: block; width: 4px; height: 4px; border-radius: 50%; background: currentColor; }
  .rule-bottom .dots i.mid { width: 6px; height: 6px; margin-top: -1px; }

  .logo-panel { position: absolute; left: 415px; top: 63px; width: 378px; height: 297px; background: var(--paper); color: var(--rule); }
  .logo-panel .brand-disc { left: 117px; top: 30px; width: 144px; height: 144px; }
  .logo-panel .rule { left: 36px; right: 36px; }
  .logo-panel .rule-top { top: 183px; }
  .logo-panel .rule-bottom { top: 246px; }
  .logo-panel .wordmark { position: absolute; left: 0; right: 0; top: 197px; font-size: 38px; color: #333; }

  .card { position: absolute; width: 527px; height: 341px; border-radius: 34px; overflow: hidden; }
  .card-front { background: var(--paper); box-shadow: 0 8px 18px rgba(0,0,0,.18); color: var(--rule); }
  .card-back { background: radial-gradient(ellipse at 50% 45%, var(--ocean-glow) 0%, #4b98b0 45%, var(--ocean) 85%); box-shadow: 0 8px 18px rgba(0,0,0,.22); color: var(--teal-light); }

  .card-front .brand-disc { left: 79px; top: 36px; width: 112px; height: 112px; }
  .card-front .rule { left: 21px; width: 228px; }
  .card-front .rule-top { top: 156px; }
  .card-front .rule-bottom { top: 207px; }
  .card-front .wordmark { position: absolute; left: 21px; width: 228px; top: 168px; font-size: 29px; color: #333; }
  .card-front .slogan { position: absolute; left: 21px; width: 228px; top: 222px; font-size: 27px; color: var(--teal); }

  .holder { position: absolute; left: 338px; top: 84px; font-size: 20px; font-weight: 600; white-space: nowrap; color: var(--ink); }
  .contact { position: absolute; left: 338px; top: 140px; list-style: none; font-size: 14px; line-height: 22px; color: var(--ink); }
  .contact li { display: flex; align-items: center; white-space: nowrap; }
  .contact svg { width: 16px; height: 16px; margin-right: 10px; flex: none; }
  .contact .indent { padding-left: 26px; }

  .divider { position: absolute; left: 16px; right: 16px; top: 291px; }

  .social { position: absolute; left: 0; right: 0; top: 305px; display: flex; justify-content: center; gap: 22px; font-size: 14px; color: var(--ink); }
  .social li { list-style: none; display: flex; align-items: center; white-space: nowrap; }
  .social li::before { content: ""; width: 12px; height: 12px; border-radius: 50%; background: var(--pink); margin-right: 7px; }

  .card-back .brand-disc { left: 201px; top: 40px; width: 124px; height: 124px; background: var(--teal-light); }
  .card-back .rule { left: 112px; width: 308px; }
  .card-back .rule-top { top: 187px; }
  .card-back .rule-bottom { top: 257px; }
  .card-back .wordmark { position: absolute; left: 0; right: 0; top: 203px; font-size: 38px; color: var(--teal-light); }
  .card-back .slogan { position: absolute; left: 0; right: 0; top: 274px; font-size: 38px; color: #e8f6f7; }

  .stage { position: absolute; left: 51px; width: 1091px; height: 727px; background: var(--stage); }
  .stage-one { top: 849px; }
  .stage-two { top: 1612px; }
  .stage .card { left: 282px; top: 193px; transform: scale(1.25); transform-origin: 50% 50%; }
</style>
</head>
<body>

<section class="logo-panel">
  <div class="brand-disc"></div>
  <div class="rule rule-top"></div>
  <div class="wordmark">Zuckerfuchs</div>
  <div class="rule rule-bottom"><span class="dots"><i></i><i class="mid"></i><i></i></span></div>
</section>

<article class="card card-front" style="left:53px; top:442px;">
  <div class="brand-disc"></div>
  <div class="rule rule-top"></div>
  <div class="wordmark">Zuckerfuchs</div>
  <div class="rule rule-bottom"><span class="dots"><i></i><i class="mid"></i><i></i></span></div>
  <div class="slogan">Süßigkeiten aus aller Welt</div>
  <h2 class="holder">Jonas Brettel</h2>
  <ul class="contact">
    <li><svg viewBox="0 0 16 16"><path d="M8 1a5 5 0 0 0-5 5c0 4 5 9 5 9s5-5 5-9a5 5 0 0 0-5-5zm0 7a2 2 0 1 1 0-4 2 2 0 0 1 0 4z" fill="var(--teal)"/></svg>Lindauer Weg 14</li>
    <li class="indent">41562 Rabenfeld</li>
    <li><svg viewBox="0 0 16 16"><path d="M4 1l3 3-2 2c1 2 3 4 5 5l2-2 3 3-2 3C7 14 2 9 1 3z" fill="var(--teal)"/></svg>01520 7734019</li>
    <li><svg viewBox="0 0 16 16"><rect x="1" y="3" width="14" height="10" fill="var(--teal)"/><path d="M1 3l7 6 7-6" stroke="#fff" stroke-width="1.3" fill="none"/></svg>info@zuckerfuchs-shop.de</li>
    <li><svg viewBox="0 0 16 16" fill="none" stroke="var(--teal)" stroke-width="1.3"><circle cx="8" cy="8" r="6.5"/><ellipse cx="8" cy="8" rx="3" ry="6.5"/><path d="M1.5 8h13M2.5 5h11M2.5 11h11"/></svg>www.zuckerfuchs-shop.de</li>
  </ul>
  <div class="rule rule-bottom divider"><span class="dots"><i></i><i class="mid"></i><i></i></span></div>
  <ul class="social">
    <li>Zuckerfuchs</li>
    <li>@zuckerfuchs.de</li>
    <li>@zuckerfuhcs.de</li>
  </ul>
</article>

<article class="card card-back" style="left:611px; top:446px;">
  <div class="brand-disc"></div>
  <div class="rule rule-top"></div>
  <div class="wordmark">Zuckerfuchs</div>
  <div class="rule rule-bottom"><span class="dots"><i></i><i class="mid"></i><i></i></span></div>
  <div class="slogan">Süßigkeiten aus aller Welt</div>
</article>

<section class="stage stage-one">
  <article class="card card-back">
    <div class="brand-disc"></div>
    <div class="rule rule-top"></div>
    <div class="wordmark">Zuckerfuchs</div>
    <div class="rule rule-bottom"><span class="dots"><i></i><i class="mid"></i><i></i></span></div>
    <div class="slogan">Süßigkeiten aus aller Welt</div>
  </article>
</section>

<section class="stage stage-two">
  <article class="card card-front">
    <div class="brand-disc"></div>
    <div class="rule rule-top"></div>
    <div class="wordmark">Zuckerfuchs</div>
    <div class="rule rule-bottom"><span class="dots"><i></i><i class="mid"></i><i></i></span></div>
    <div class="slogan">Süßigkeiten aus aller Welt</div>
    <h2 class="holder">Jonas Brettel</h2>
    <ul class="contact">
      <li><svg viewBox="0 0 16 16"><path d="M8 1a5 5 0 0 0-5 5c0 4 5 9 5 9s5-5 5-9a5 5 0 0 0-5-5zm0 7a2 2 0 1 1 0-4 2 2 0 0 1 0 4z" fill="var(--teal)"/></svg>Lindauer Weg 14</li>
      <li class="indent">41562 Rabenfeld</li>
      <li><svg viewBox="0 0 16 16"><path d="M4 1l3 3-2 2c1 2 3 4 5 5l2-2 3 3-2 3C7 14 2 9 1 3z" fill="var(--teal)"/></svg>01520 7734019</li>
      <li><svg viewBox="0 0 16 16"><rect x="1" y="3" width="14" height="10" fill="var(--teal)"/><path d="M1 3l7 6 7-6" stroke="#fff" stroke-width="1.3" fill="none"/></svg>info@zuckerfuchs-shop.de</li>
      <li><svg viewBox="0 0 16 16" fill="none" stroke="var(--teal)" stroke-width="1.3"><circle cx="8" cy="8" r="6.5"/><ellipse cx="8" cy="8" rx="3" ry="6.5"/><path d="M1.5 8h13M2.5 5h11M2.5 11h11"/></svg>www.zuckerfuchs-shop.de</li>
    </ul>
    <div class="rule rule-bottom divider"><span class="dots"><i></i><i class="mid"></i><i></i></span></div>
    <ul class="social">
      <li>Zuckerfuchs</li>
      <li>@zuckerfuchs.de</li>
      <li>@zuckerfuhcs.de</li>
    </ul>
  </article>
</section>

</body>
</html>
```